Yard Sign Design Needed

Yard sign needed for mowing & landscaping company. Would like to use the top logo with black background which is attached. Would like MOWING to be in large standout letters. The word "landscaping" can be smaller and more artistic or omitted. Will need room for phone number once design is approved. The phone number will need to stand out and look identical/similar to the word 'MOWING"

```html
<!DOCTYPE html>
<html lang="en">
<head>
<meta charset="utf-8">
<title>Norvale Contractors – Mowing Yard Sign</title>
<link rel="stylesheet" href="https://fonts.googleapis.com/css2?family=Michroma&family=Exo+2:wght@400;600&display=swap">
<style>
  :root {
    --page-bg: #e9ebe6;
    --sign-black: #000000;
    --sign-white: #ffffff;
    --lime-light: #c6e84a;
    --lime-mid: #9cc61e;
    --lime-dark: #6f9412;
    --text-white: #ffffff;
  }
  * { margin: 0; padding: 0; box-sizing: border-box; }
  html, body {
    width: 1200px;
    height: 1000px;
    overflow: hidden;
    background: var(--page-bg);
  }
  .yard-sign {
    position: absolute;
    left: 50px;
    top: 134px;
    width: 1100px;
    height: 732px;
    display: flex;
    flex-direction: column;
    box-shadow: 0 6px 24px rgba(0,0,0,0.18);
  }
  .sign-top {
    position: relative;
    height: 568px;
    background: var(--sign-black);
  }
  .sign-bottom {
    position: relative;
    flex: 1;
    background: var(--sign-white);
  }
  .brand {
    position: absolute;
    top: 60px;
    left: 0;
    right: 0;
    display: flex;
    flex-direction: column;
    align-items: center;
    gap: 18px;
  }
  .brand-mark {
    width: 64px;
    height: 64px;
    background: var(--lime-mid);
  }
  .brand-name {
    font-family: "Exo 2", sans-serif;
    font-weight: 600;
    color: var(--lime-mid);
    text-align: center;
    line-height: 1.05;
    letter-spacing: 2px;
  }
  .brand-name .brand-line-main { display: block; font-size: 40px; letter-spacing: 3px; }
  .brand-name .brand-line-sub { display: block; font-size: 26px; }
  .headline {
    position: absolute;
    left: 70px;
    top: 330px;
    width: 930px;
    height: 110px;
  }
  .service-secondary {
    position: absolute;
    left: 0;
    right: 0;
    top: 452px;
    text-align: center;
    font-family: "Exo 2", sans-serif;
    font-weight: 400;
    font-size: 58px;
    letter-spacing: 6px;
    color: var(--text-white);
  }
  .phone {
    position: absolute;
    left: 60px;
    top: 40px;
    width: 960px;
    height: 80px;
  }
  .headline text, .phone text {
    font-family: "Michroma", sans-serif;
  }
</style>
</head>
<body>
  <main class="yard-sign">
    <section class="sign-top">
      <div class="brand">
        <div class="brand-mark"></div>
        <div class="brand-name">
          <span class="brand-line-main">NORVALE</span>
          <span class="brand-line-sub">CONTRACTORS LLC</span>
        </div>
      </div>

      <svg class="headline" viewBox="0 0 930 110" aria-label="Mowing">
        <defs>
          <linearGradient id="limeFade" x1="0" y1="0" x2="0" y2="1">
            <stop offset="0" stop-color="var(--lime-light)"/>
            <stop offset="0.55" stop-color="var(--lime-mid)"/>
            <stop offset="1" stop-color="var(--lime-dark)"/>
          </linearGradient>
        </defs>
        <text x="0" y="96" font-size="104" textLength="920" lengthAdjust="spacingAndGlyphs" fill="url(#limeFade)">MOWING</text>
      </svg>

      <p class="service-secondary">LANDSCAPING</p>
    </section>

    <section class="sign-bottom">
      <svg class="phone" viewBox="0 0 960 80" aria-label="Phone number 123-456-78910">
        <defs>
          <linearGradient id="limeFadePhone" x1="0" y1="0" x2="0" y2="1">
            <stop offset="0" stop-color="var(--lime-light)"/>
            <stop offset="0.55" stop-color="var(--lime-mid)"/>
            <stop offset="1" stop-color="var(--lime-dark)"/>
          </linearGradient>
        </defs>
        <text x="0" y="66" font-size="60" textLength="955" lengthAdjust="spacingAndGlyphs" fill="url(#limeFadePhone)">123-456-78910</text>
      </svg>
    </section>
  </main>
</body>
</html>
```